依頼詳細
お客様と話をする際、代理店や営業マンがお客様にお見せして、瞬時にポイントがわかり、詳細まで見たくなる仕上がりにしたいと考えています。
記載項目
文字、文言は添付ファイルにでています。
記載したい文字や協調したい文言は、文字の大きさで表現していますので、参考
にしてください。
表面
配置や色使いはお任せ致します。ポイントが目に飛び込んでくる様な仕上げに
してください。
裏面
事例が4例でてます。ポイントは赤字にしてありますが、元の配置や文字ポイン
ト・色は無視
して頂いて結構です。ポイントがわかりやすい仕上がりでお願い致します。
グラフについても同様で、意味が同じであればどんな色でもOKです。

サイズ
A4
ページ数
両面
希望イメージ
シンプル 複雑
単色 カラフル
暗い 明るい
日常 高級
遊び心 厳粛
未来的 伝統的
女性的 男性的
希望する色
水色系、グレー系
納品ファイル
• イラストレーター形式 (.ai)
補足説明
構成やデザインについての変更は、ありませんが文字(数値)などの変更をお願いする事がありますので、その節には対応の程お願い致します。
ロゴは、aiファイルに貼ってあります。
■ 選んだ理由

本当に悩みましたが
今回の利用目的を考慮した結果です。

■ 提案者全員のお礼・コメント

本当に、迷いました。
また機会がございましたら、是非ご応募いただきます様お願い致します。
皆さま方の今後の活躍を期待しております。

```html
<!DOCTYPE html>
<html lang="ja">
<head>
<meta charset="utf-8">
<title>電気代削減のご提案</title>
<link href="https://fonts.googleapis.com/css2?family=Noto+Sans+JP:wght@400;500;700;900&display=swap" rel="stylesheet">
<style>
  :root {
    --sky-top: #bfe3f5;
    --sky-bottom: #f4fafd;
    --green: #5bb431;
    --blue: #1c7fc2;
    --steel: #7b9dbd;
    --roof: #9ea8b1;
    --ink: #333a40;
    --red: #d7262b;
    --panel-dark: #4b5259;
    --facade-light: #e3e7ea;
    --facade-dark: #c3c9ce;
    --white: #ffffff;
  }
  * { margin: 0; padding: 0; box-sizing: border-box; }
  html, body { width: 848px; height: 1200px; overflow: hidden; }
  body { font-family: "Noto Sans JP", sans-serif; color: var(--ink); background: var(--white); }
  .poster {
    position: relative; width: 848px; height: 1200px; overflow: hidden;
    background: linear-gradient(180deg, var(--sky-top) 0%, var(--sky-bottom) 55%, var(--white) 100%);
  }
  .shapes { position: absolute; inset: 0; }
  .vertical { position: absolute; writing-mode: vertical-rl; font-weight: 900; color: var(--white); line-height: 1; }
  .banner-title { font-size: 96px; letter-spacing: 2px; }
  .banner-sub { font-size: 34px; font-weight: 700; }
  .banner-note { font-size: 19px; font-weight: 700; color: var(--ink); transform: rotate(-8deg); }
  .left-title { left: 110px; top: 36px; }
  .left-sub { left: 226px; top: 40px; }
  .left-note { left: 282px; top: 290px; }
  .right-sub { left: 582px; top: 40px; }
  .right-title { left: 640px; top: 36px; font-size: 104px; }

  .pitch {
    position: absolute; left: 284px; top: 58px; width: 280px; height: 140px;
    background: var(--white); border-radius: 14px;
    display: flex; flex-direction: column; justify-content: center; align-items: center;
    font-size: 22px; font-weight: 700; line-height: 1.5; text-align: center;
    box-shadow: 0 3px 8px rgba(0,0,0,0.08);
  }
  .pitch .accent { color: var(--blue); }
  .bulb {
    position: absolute; left: 394px; top: 240px; width: 60px; height: 80px; border-radius: 30px 30px 14px 14px;
    background: radial-gradient(circle at 50% 38%, #fff8c8 0%, #f4d35e 60%, #c9c9c9 100%);
  }
  .reduce {
    position: absolute; left: 0; width: 848px; top: 450px; text-align: center;
    font-size: 108px; font-weight: 900; color: var(--steel); letter-spacing: 14px; line-height: 1.2;
    -webkit-text-stroke: 3px var(--white); paint-order: stroke fill;
  }

  .facade {
    position: absolute; left: 40px; top: 600px; width: 768px; height: 530px;
    background: linear-gradient(180deg, var(--facade-light) 0%, var(--facade-dark) 100%);
  }
  .headline-card {
    position: absolute; left: 226px; top: 662px; width: 412px; height: 86px;
    background: var(--white); text-align: center; padding-top: 14px;
  }
  .tag {
    position: absolute; left: 82px; top: -18px; padding: 2px 24px;
    background: var(--red); color: var(--white); border-radius: 18px; font-size: 20px; font-weight: 700;
  }
  .headline { font-size: 25px; font-weight: 900; line-height: 1.3; }
  .headline .hit { color: var(--red); }

  .tubes {
    position: absolute; left: 110px; top: 770px; width: 270px; height: 140px;
    background: linear-gradient(180deg, #f7f7f7 0%, #d4d9dc 100%);
  }
  .case-text {
    position: absolute; left: 396px; top: 772px; width: 340px;
    font-size: 14px; line-height: 1.75; font-weight: 500;
  }
  .case-text .hit { color: var(--red); font-weight: 700; }

  .about {
    position: absolute; left: 100px; top: 940px; width: 650px; height: 150px;
    background: var(--panel-dark); color: var(--white);
    padding: 22px 26px; font-size: 14.5px; line-height: 1.8;
  }

  .footer {
    position: absolute; left: 0; top: 1130px; width: 848px; height: 70px; background: var(--white);
    display: flex; align-items: center; justify-content: space-between; padding: 0 40px;
  }
  .brand { font-size: 26px; font-weight: 900; color: var(--ink); }
  .company { text-align: right; font-size: 15px; font-weight: 700; line-height: 1.5; }
</style>
</head>
<body>
<div class="poster">
  <svg class="shapes" width="848" height="1200" viewBox="0 0 848 1200">
    <polygon points="15,0 330,0 330,410 15,560" fill="var(--green)"/>
    <polygon points="518,0 833,0 833,560 518,410" fill="var(--green)"/>
    <polyline points="0,598 424,392 848,598" fill="none" stroke="var(--roof)" stroke-width="16"/>
  </svg>

  <div class="vertical banner-title left-title">消費電力</div>
  <div class="vertical banner-sub left-sub">LED交換で消費電力削減</div>
  <div class="vertical banner-note left-note">工事費も安い!</div>
  <div class="vertical banner-sub right-sub">新電力導入で電気代削減</div>
  <div class="vertical banner-title right-title">電気代</div>

  <div class="pitch">
    <span>省エネ診断ができる</span>
    <span>新電力会社からの</span>
    <span class="accent">電気代削減の提案</span>
  </div>
  <div class="bulb" role="img" aria-label="光る電球のイラスト"></div>

  <div class="facade" role="img" aria-label="照明が灯るオフィスビルの外観イラスト"></div>
  <div class="reduce">削減</div>

  <div class="headline-card">
    <span class="tag">さらに</span>
    <p class="headline">LED 導入による<br>管球交換コスト<span class="hit">も削減</span></p>
  </div>

  <div class="tubes" role="img" aria-label="LED 直管ランプのイラスト"></div>
  <p class="case-text">
    蛍光灯の寿命が 10,000 時間、LED の寿命が 40,000 時間とした場合交換費用は約 4 分の 1。日数経過の場合はさらに短く約 2,000 時間とした場合<span class="hit">交換費用は約 20 分の1</span>。交換箇所が 100 箇所の場合の費用を計算すると大きな節約となります。
  </p>

  <p class="about">
    アオバ電力の関連団体は、国・自治体・みどり環境ネット・省エネ推進協会各機関の無料省エネ診断の診断事業者です。数多くの診断の実績がある新電力会社だからこそ、お客様の立場で考え最もお客様が喜ぶ提案をする事ができるのです。
  </p>

  <footer class="footer">
    <div class="brand">アオバ電力</div>
    <div class="company">株式会社青葉ライトワークス<br>東京都千代田区神田 1-2-3</div>
  </footer>
</div>
</body>
</html>
```